Full re-design of visual identity

We have just re-designed our logo and would like to apply it on our folders, business cards, stationery, and etc... we are attaching new logo + the material we need to re-design... we will provide full corel draw files to help make job easier and also because lot of icons and artwork can be still used...

any doubts we are at your disposal. thanks in advance.

```html
<!DOCTYPE html>
<html lang="en">
<head>
<meta charset="utf-8">
<title>Corvalo stationery set</title>
<link rel="stylesheet" href="https://fonts.googleapis.com/css2?family=Roboto:wght@400;700&family=Tinos:wght@400;700&display=swap">
<style>
  :root {
    --orange: #e4650f;
    --orange-deep: #c94f06;
    --ink: #5a5a5a;
    --dark: #1f1f1f;
    --paper: #ffffff;
    --backdrop: #f3f3f3;
    --edge: #e2e2e2;
    --muted: #8a8a8a;
  }
  * { box-sizing: border-box; margin: 0; padding: 0; }
  html, body { width: 1200px; height: 795px; overflow: hidden; }
  body { background: var(--backdrop); font-family: "Roboto", sans-serif; color: var(--ink); }
  .canvas { position: relative; width: 1200px; height: 795px; }
  .sheet { position: absolute; background: var(--paper); border: 1px solid var(--edge); overflow: hidden; }
  .sheet svg.swoosh { position: absolute; left: 0; bottom: 0; }
  .wordmark { font-family: "Roboto", sans-serif; font-weight: 700; color: var(--ink); letter-spacing: -0.5px; display: flex; align-items: center; line-height: 1; }
  .wordmark .dot { display: inline-block; border-radius: 50%; background: var(--orange); margin-left: 4px; }
  .tagline { font-size: 4px; color: var(--muted); letter-spacing: 0.3px; margin-top: 2px; white-space: nowrap; }

  /* letterhead */
  .letterhead { left: 298px; top: 38px; width: 274px; height: 370px; }
  .letterhead .brand { position: absolute; left: 46px; top: 24px; }
  .letterhead .wordmark { font-size: 20px; }
  .letterhead .wordmark .dot { width: 9px; height: 9px; }
  .letter-body { position: absolute; left: 40px; top: 80px; width: 212px; font-family: "Tinos", serif; font-size: 5.8px; line-height: 1.3; color: var(--dark); text-align: justify; }
  .letter-body p { margin-bottom: 6px; }
  .letter-body .salutation { font-style: italic; margin-bottom: 8px; }
  .letter-body .sign-off { margin-top: 40px; text-align: left; }
  .signature { display: block; width: 36px; height: 12px; background: #d9d9d9; margin: 3px 0; }
  .contact-list { position: absolute; left: 32px; top: 330px; list-style: none; font-size: 4px; color: var(--muted); line-height: 1.7; }
  .contact-list li::before { content: ""; display: inline-block; width: 3px; height: 3px; background: var(--orange); border-radius: 1px; margin-right: 5px; vertical-align: middle; }

  /* folder */
  .folder { left: 597px; top: 36px; width: 315px; height: 384px; }
  .folder .brand { position: absolute; left: 94px; top: 64px; }
  .folder .wordmark { font-size: 30px; }
  .folder .wordmark .dot { width: 13px; height: 13px; }
  .folder .tagline { font-size: 6px; margin-left: 6px; }

  /* business cards */
  .card-front { left: 295px; top: 440px; width: 118px; height: 60px; }
  .card-front .brand { position: absolute; left: 14px; top: 8px; }
  .card-front .wordmark { font-size: 12px; }
  .card-front .wordmark .dot { width: 5px; height: 5px; }
  .card-person { position: absolute; right: 20px; top: 22px; font-family: "Tinos", serif; font-size: 4.4px; color: var(--dark); }
  .card-person .role { color: var(--orange); display: block; }
  .card-front .contact-list { left: 14px; top: 31px; font-size: 3px; line-height: 1.55; }
  .card-front .contact-list li::before { width: 2px; height: 2px; margin-right: 3px; }
  .card-back { left: 453px; top: 435px; width: 119px; height: 67px; }
  .card-back .brand { position: absolute; left: 12px; bottom: 10px; }
  .card-back .wordmark { font-size: 12px; }
  .card-back .wordmark .dot { width: 5px; height: 5px; }
  .card-back .mark-circle { position: absolute; right: 14px; top: 8px; width: 26px; height: 26px; border-radius: 50%; background: var(--orange); }

  /* envelopes */
  .envelope { left: 612px; top: 447px; width: 293px; height: 143px; }
  .envelope .seal { position: absolute; left: 138px; top: 14px; width: 16px; height: 16px; border-radius: 50%; background: var(--orange); }
  .envelope-dl { left: 612px; top: 612px; width: 293px; height: 150px; }
  .envelope-dl .brand { position: absolute; left: 30px; top: 20px; }
  .envelope-dl .wordmark { font-size: 21px; }
  .envelope-dl .wordmark .dot { width: 9px; height: 9px; }

  /* notebook */
  .notebook { left: 292px; top: 562px; width: 136px; height: 198px; }
  .notebook .brand { position: absolute; left: 32px; top: 88px; }
  .notebook .wordmark { font-size: 16px; }
  .notebook .wordmark .dot { width: 7px; height: 7px; }
  .spiral { position: absolute; left: 286px; top: 566px; }

  /* small items */
  .keytag { left: 466px; top: 580px; width: 38px; height: 84px; border-radius: 8px; }
  .keytag .brand { position: absolute; left: 7px; top: 40px; }
  .keytag .wordmark { font-size: 8px; }
  .keytag .wordmark .dot { width: 3px; height: 3px; margin-left: 2px; }
  .keytag .mark-circle { position: absolute; left: 13px; top: 22px; width: 11px; height: 11px; border-radius: 50%; background: var(--orange); }
  .key-ring { position: absolute; left: 470px; top: 540px; }
  .eraser { left: 476px; top: 680px; width: 25px; height: 80px; border-radius: 2px; }
  .eraser .mark-circle { position: absolute; left: 7px; top: 40px; width: 11px; height: 11px; border-radius: 50%; background: var(--orange); }
</style>
</head>
<body>
<main class="canvas">

  <article class="sheet letterhead">
    <div class="brand">
      <div class="wordmark">corvalo<span class="dot"></span></div>
      <div class="tagline">network · cloud · fiber</div>
    </div>
    <div class="letter-body">
      <p class="salutation">Dear Partners,</p>
      <p>Enclosed you will find our latest service overview, which we would be glad to share with your team. Our network upgrade is now complete across the region, and we are ready to support your projects with faster links and steady care. Please let us know a suitable date for a short meeting, and we will arrange all details on our side.</p>
      <p>We thank you for the trust you have shown in our work over the past years. Our support desk remains open every day, and our engineers are always ready to answer your questions. We look forward to building the next stage of our network together and to seeing you soon.</p>
      <p class="sign-off">With kind regards,<br>Yours truly,
        <span class="signature" role="img" aria-label="Handwritten signature"></span>
        <strong>Martin Hale</strong></p>
    </div>
    <ul class="contact-list">
      <li>(011) 555-0142</li>
      <li>(011) 555-0143</li>
      <li>hello@corvalo.net</li>
      <li>www.corvalo.net</li>
    </ul>
    <svg class="swoosh" width="274" height="30" viewBox="0 0 274 30" aria-hidden="true">
      <path d="M60 30 Q170 4 274 6 L274 30 Z" fill="var(--orange)"/>
      <path d="M110 30 Q200 12 274 14 L274 30 Z" fill="var(--orange-deep)"/>
    </svg>
  </article>

  <article class="sheet folder">
    <svg width="315" height="384" viewBox="0 0 315 384" style="position:absolute;left:0;top:0" aria-hidden="true">
      <path d="M0 0 H250 Q110 6 0 22 Z" fill="var(--orange-deep)"/>
      <path d="M0 196 Q150 146 315 150 L315 384 L0 384 Z" fill="var(--orange)"/>
    </svg>
    <div class="brand">
      <div class="wordmark">corvalo<span class="dot"></span></div>
      <div class="tagline">network · cloud · fiber</div>
    </div>
  </article>

  <article class="sheet card-front">
    <div class="brand">
      <div class="wordmark">corvalo<span class="dot"></span></div>
    </div>
    <div class="card-person">Lena Moretti<span class="role">Director</span></div>
    <ul class="contact-list">
      <li>(011) 555-0142</li>
      <li>(011) 555-0143</li>
      <li>hello@corvalo.net</li>
      <li>www.corvalo.net</li>
    </ul>
    <svg class="swoosh" width="118" height="12" viewBox="0 0 118 12" aria-hidden="true">
      <path d="M20 12 Q70 2 118 3 L118 12 Z" fill="var(--orange)"/>
    </svg>
  </article>

  <article class="sheet card-back">
    <span class="mark-circle"></span>
    <div class="brand">
      <div class="wordmark">corvalo<span class="dot"></span></div>
    </div>
  </article>

  <article class="sheet envelope">
    <svg width="293" height="143" viewBox="0 0 293 143" style="position:absolute;left:0;top:0" aria-hidden="true">
      <path d="M0 0 L14 46 H279 L293 0" fill="none" stroke="var(--edge)" stroke-width="1"/>
    </svg>
    <span class="seal"></span>
  </article>

  <article class="sheet envelope-dl">
    <div class="brand">
      <div class="wordmark">corvalo<span class="dot"></span></div>
      <div class="tagline">network · cloud · fiber</div>
    </div>
    <svg class="swoosh" width="293" height="24" viewBox="0 0 293 24" aria-hidden="true">
      <path d="M90 24 Q190 4 293 6 L293 24 Z" fill="var(--orange)"/>
    </svg>
  </article>

  <article class="sheet notebook">
    <div class="brand">
      <div class="wordmark">corvalo<span class="dot"></span></div>
      <div class="tagline">network · cloud · fiber</div>
    </div>
  </article>
  <svg class="spiral" width="12" height="192" viewBox="0 0 12 192" aria-hidden="true">
    <g stroke="#444" stroke-width="1.2" fill="none">
      <path d="M2 4h8M2 10h8M2 16h8M2 22h8M2 28h8M2 34h8M2 40h8M2 46h8M2 52h8M2 58h8M2 64h8M2 70h8M2 76h8M2 82h8M2 88h8M2 94h8M2 100h8M2 106h8M2 112h8M2 118h8M2 124h8M2 130h8M2 136h8M2 142h8M2 148h8M2 154h8M2 160h8M2 166h8M2 172h8M2 178h8M2 184h8"/>
    </g>
  </svg>

  <svg class="key-ring" width="30" height="42" viewBox="0 0 30 42" aria-hidden="true">
    <circle cx="15" cy="14" r="11" fill="none" stroke="#9a9a9a" stroke-width="2"/>
    <path d="M15 25 V40" stroke="#9a9a9a" stroke-width="2"/>
  </svg>
  <article class="sheet keytag">
    <span class="mark-circle"></span>
    <div class="brand"><div class="wordmark">corvalo<span class="dot"></span></div></div>
  </article>

  <article class="sheet eraser">
    <span class="mark-circle"></span>
  </article>

</main>
</body>
</html>
```